Need a business card design for a residential architect.

You can get a sense of his work at www.tbrelloway.com

Would like a consistent look and feel between business card and website
.

Target Market(s)

Residential homeowners builders

Industry/Entity Type

Residential

Contact Information for Business Card

Dale Brelloway
Principle
Brelloway Architecture
418 Quillfern Lane
Larkhaven, CA 94990

dale@tbrelloway.com

tbrelloway.com
phone: 650-555-0172
Fax: 650-555-0194

Font styles to use
Sans Serif

Requirements
Must have
• Details above
Nice to have
• Would like a consistent look and feel between business card and website
Should not have
• None

```html
<!DOCTYPE html>
<html lang="en">
<head>
<meta charset="utf-8">
<title>Brelloway Architecture – Business Card</title>
<link rel="stylesheet" href="https://fonts.googleapis.com/css2?family=Source+Sans+3:wght@400;700&display=swap">
<style>
  :root {
    --bg: #e6e4e1;
    --card-white: #ffffff;
    --ink: #111111;
    --logo-grey: #8f8f8f;
    --rule-grey: #a8a8a8;
    --steel-dark: #8c8c8c;
    --steel-mid: #a3a3a3;
    --steel-light: #c9c9c9;
    --logo-white: #ffffff;
    --lawn-green: #5f9a3a;
    --sky-blue: #9cc4e8;
    --villa-ochre: #c9a94e;
    --pool-blue: #1436a8;
    --deep-blue: #0a1f78;
    --terrace: #d9d2c3;
  }
  * { margin: 0; padding: 0; box-sizing: border-box; }
  html, body {
    width: 1200px; height: 1000px; overflow: hidden;
    background: var(--bg);
    font-family: "Source Sans 3", sans-serif;
  }
  .canvas { position: relative; width: 1200px; height: 1000px; }

  .card {
    position: absolute;
    width: 690px; height: 410px;
    overflow: hidden;
    box-shadow: 0 6px 18px rgba(0,0,0,0.25);
  }

  /* Front */
  .card-front { left: 70px; top: 80px; background: var(--card-white); }
  .wordmark {
    position: absolute; left: 60px; top: 58px;
    color: var(--logo-grey); font-weight: 400; line-height: 1;
  }
  .wordmark-name { display: block; font-size: 56px; letter-spacing: 1px; }
  .wordmark-sub { display: block; font-size: 19px; letter-spacing: 10.5px; margin-top: 6px; }
  .divider {
    position: absolute; left: 60px; top: 160px;
    width: 320px; height: 2px; background: var(--rule-grey);
  }
  .contact-primary {
    position: absolute; left: 62px; top: 190px;
    font-weight: 700; font-size: 23px; line-height: 1.3; color: var(--ink);
  }
  .contact-details {
    position: absolute; left: 64px; top: 292px;
    font-weight: 400; font-size: 18px; line-height: 1.35; color: var(--ink);
  }
  .contact-web {
    position: absolute; left: 64px; top: 370px;
    font-weight: 700; font-size: 22px; line-height: 1; color: var(--ink);
  }
  .photo { position: absolute; }
  .photo-villa {
    left: 458px; top: 96px; width: 218px; height: 72px;
    background: linear-gradient(180deg, var(--sky-blue) 0%, var(--sky-blue) 30%, var(--villa-ochre) 55%, var(--lawn-green) 75%, var(--lawn-green) 100%);
  }
  .photo-pool {
    left: 462px; top: 176px; width: 210px; height: 192px;
    background: linear-gradient(180deg, var(--pool-blue) 0%, var(--sky-blue) 40%, var(--terrace) 60%, var(--pool-blue) 72%, var(--deep-blue) 100%);
  }

  /* Back */
  .card-back {
    left: 450px; top: 530px;
    background: linear-gradient(115deg, var(--steel-dark) 0%, var(--steel-mid) 35%, var(--steel-light) 50%, var(--steel-mid) 62%, var(--steel-dark) 100%);
  }
  .card-back .wordmark { left: 60px; top: 34px; color: var(--logo-white); }
</style>
</head>
<body>
<main class="canvas">
  <section class="card card-front" aria-label="Business card front">
    <div class="wordmark">
      <span class="wordmark-name">BRELLOWAY</span>
      <span class="wordmark-sub">ARCHITECTURE</span>
    </div>
    <div class="divider"></div>
    <div class="contact-primary">
      <p>Dale Brelloway Principle</p>
      <p>650-555-0172</p>
    </div>
    <div class="contact-details">
      <p>418 Quillfern Lane Larkhaven, CA 94990</p>
      <p>email: dale@tbrelloway.com</p>
      <p>fax: 650-555-0194</p>
    </div>
    <p class="contact-web">tbrelloway.com</p>
    <div class="photo photo-villa" role="img" aria-label="Photo of an ochre villa with lawn and trees under a blue sky"></div>
    <div class="photo photo-pool" role="img" aria-label="Photo of a large house behind a terrace and blue swimming pool"></div>
  </section>

  <section class="card card-back" aria-label="Business card back">
    <div class="wordmark">
      <span class="wordmark-name">BRELLOWAY</span>
      <span class="wordmark-sub">ARCHITECTURE</span>
    </div>
  </section>
</main>
</body>
</html>
```